Business Card Design Project 4 Construction Business

I am after a creative, but sleek and simple/ clean business card design. This design will form the basis of future items and might include a logo or simply a creative way to lay out the text of my company name 'kestrel ventures'
I like the simplicity of black and white however I would also be happy to see a splash of colour introduced somehow to give the text some interest and make it stand out.
I would like a double sided card.
I am young (ish!) and professional, offering construction and project management services, what I don't want is the traditional builders type card featuring a cheesy hammer/ saw image etc.
As the company name, kestrel ventures, suggests, we focus on working closely and collaboratively together, in synergy with all stakeholders involved in the projects that we undertake
Construction

```html
<!DOCTYPE html>
<html lang="en">
<head>
<meta charset="utf-8">
<title>Kestrel Ventures – Business Card</title>
<link rel="stylesheet" href="https://fonts.googleapis.com/css2?family=Montserrat:wght@600&family=Cinzel:wght@600&family=Open+Sans:wght@400;600&display=swap">
<style>
  :root {
    --stage: #e4e6e8;
    --paper: #ffffff;
    --paper-shade: #e9e9e9;
    --ink: #2f2f2f;
    --charcoal: #3b3b3b;
    --skyline: #232323;
    --light-text: #f2f2f2;
    --muted-text: #cfcfcf;
  }
  * { margin: 0; padding: 0; box-sizing: border-box; }
  html, body { width: 1200px; height: 960px; overflow: hidden; }
  body {
    background: var(--stage);
    display: flex;
    flex-direction: column;
    align-items: center;
    justify-content: center;
    gap: 32px;
    font-family: "Open Sans", Arial, sans-serif;
  }
  .card {
    position: relative;
    width: 760px;
    height: 434px;
    overflow: hidden;
    box-shadow: 0 6px 18px rgba(0,0,0,0.18);
  }

  /* Front */
  .card-front {
    background: radial-gradient(ellipse at 50% 40%, var(--paper) 45%, var(--paper-shade) 100%);
  }
  .wordmark {
    font-family: "Montserrat", Arial, sans-serif;
    font-weight: 600;
    color: var(--ink);
    text-transform: uppercase;
    line-height: 1;
  }
  .card-front .wordmark {
    position: absolute;
    left: 0; right: 0; top: 92px;
    text-align: center;
  }
  .card-front .wordmark-main { display: block; font-size: 74px; letter-spacing: 2px; }
  .card-front .wordmark-sub { display: block; font-size: 34px; letter-spacing: 12px; margin-top: 10px; padding-left: 12px; }
  .front-skyline {
    position: absolute;
    left: 170px; right: 0; bottom: 0;
    height: 128px;
  }
  .front-base {
    position: absolute;
    left: 0; right: 0; bottom: 0;
    height: 22px;
    background: var(--skyline);
  }

  /* Back */
  .card-back { background: var(--charcoal); }
  .back-header {
    position: absolute;
    left: 0; right: 0; top: 0;
    height: 110px;
    background: linear-gradient(180deg, var(--paper) 0%, var(--paper-shade) 100%);
  }
  .card-back .wordmark {
    position: absolute;
    left: 40px; top: 26px;
  }
  .card-back .wordmark-main { display: block; font-size: 34px; letter-spacing: 1px; }
  .card-back .wordmark-sub { display: block; font-size: 17px; letter-spacing: 7px; margin-top: 4px; }
  .back-skyline {
    position: absolute;
    left: 360px; right: 0; top: 50px;
    height: 80px;
  }
  .holder {
    position: absolute;
    left: 0; right: 0; top: 170px;
    text-align: center;
    font-family: "Cinzel", Georgia, serif;
    font-weight: 600;
    color: var(--light-text);
  }
  .holder-name { font-size: 34px; letter-spacing: 2px; }
  .holder-role { font-size: 20px; margin-top: 4px; text-transform: none; }
  .contact {
    position: absolute;
    left: 30px; bottom: 48px;
    list-style: none;
    font-size: 14px;
    color: var(--light-text);
  }
  .contact li { display: flex; gap: 14px; line-height: 24px; }
  .contact-label { width: 10px; font-weight: 600; }
  .address {
    position: absolute;
    right: 36px; bottom: 46px;
    text-align: right;
    font-style: normal;
    font-size: 14px;
    line-height: 22px;
    color: var(--light-text);
  }
</style>
</head>
<body>

  <section class="card card-front" aria-label="Card front">
    <h1 class="wordmark">
      <span class="wordmark-main">Kestrel</span>
      <span class="wordmark-sub">Ventures</span>
    </h1>
    <svg class="front-skyline" role="img" aria-label="City skyline silhouette illustration" viewBox="0 0 590 128" preserveAspectRatio="none">
      <rect x="0" y="0" width="590" height="128" fill="var(--skyline)"/>
    </svg>
    <div class="front-base"></div>
  </section>

  <section class="card card-back" aria-label="Card back">
    <div class="back-header"></div>
    <h2 class="wordmark">
      <span class="wordmark-main">Kestrel</span>
      <span class="wordmark-sub">Ventures</span>
    </h2>
    <svg class="back-skyline" role="img" aria-label="City skyline silhouette illustration" viewBox="0 0 400 80" preserveAspectRatio="none">
      <rect x="0" y="0" width="400" height="80" fill="var(--skyline)"/>
    </svg>

    <div class="holder">
      <p class="holder-name">OWEN CARRICK</p>
      <p class="holder-role">Director</p>
    </div>

    <ul class="contact">
      <li><span class="contact-label">T</span><span>:&nbsp; 0400 555 017</span></li>
      <li><span class="contact-label">E</span><span>:&nbsp; owen@kestrelventures.com.au</span></li>
      <li><span class="contact-label">W</span><span>:&nbsp; www.kestrelventures.com.au</span></li>
    </ul>

    <address class="address">
      14 Harlow St Brookvale<br>
      NSW 2100
    </address>
  </section>

</body>
</html>
```